Building company with a modern and unique product looking for a business card to help us stand out

We currently have a logo but as our business has grown, we feel that our business card is not reflecting our modern and high quality product and help us stand out from the crowd. Our business is mainly in the construction of new homes using a unique method and materials that makes our homes fire proof, vermin and pest resistant and rated to the maximum cyclone category (category 5). We need a business card that helps us stand out as well as communicating professionalism, high quality and trustworthiness. I have attached our current logo with a black and white option, as well as our business card which is double sided. We would like to retain as much of the information that is currently on our business cards, but presented in a more sleek way. We do like our current colour palette ( white, black, yellow and grey) and have been looking primarily at business cards with a black background however we are open to other combinations of colour and layout as long as we stand out. Please feel free to tweak our logo to make it more suitable for a business card, we like the black option that we use but we have had trouble trying to get the white area to match the rest of the logo and blend effectively into a business card. Please do not hesitate to contact us with any questions as we really want this to be successful!

Target Market(s)

Large contracts including government and larger companies

Industry/Entity Type

Business

Contact Information for Business Card

We will be providing this business card to potential clients including key government ministers and large funding companies, our business card should show that we are professional and reliable.

Requirements
Must have
• It must be easy to read and pleasing to the eye, It must contain as much of the information on the current business card and unless something really stands out, we will most likely pick a design that has all of the information included. It must include our logo of course and have some colour included.
Nice to have
• We are looking for a high end business card and would like to see designs that reflect this. We like the gloss/matte contrast, plastic cards with opaque/coloured areas and unique features not seen on everyday paper business cards. It would be nice to see a few different colour combinations, we are open to new ideas so please feel free to take some artistic licence.
Should not have
• Must not be too busy, difficult to read or be distracting from the information conveyed. Other than this please feel free to add your own touches and make it unique!

```html
<!DOCTYPE html>
<html lang="en">
<head>
<meta charset="utf-8">
<title>Tarvale Building Company – Business Card</title>
<link href="https://fonts.googleapis.com/css2?family=Montserrat:wght@700&family=Tinos:ital,wght@0,400;1,400&display=swap" rel="stylesheet">
<style>
  :root {
    --backdrop: #b9b7b8;
    --card-black: #1b1c1e;
    --gold: #cfa935;
    --white: #ffffff;
    --ink: #2a2a2a;
    --rule: #55575b;
    --light: #e9e9e9;
  }
  * { margin: 0; padding: 0; box-sizing: border-box; }
  html, body { width: 1200px; height: 1200px; overflow: hidden; }
  body {
    background: var(--backdrop);
    position: relative;
    font-family: "Tinos", "Times New Roman", serif;
  }
  .card {
    position: absolute;
    background: var(--card-black);
    border-radius: 22px;
    overflow: hidden;
    color: var(--white);
  }
  .card--front { left: 238px; top: 118px; width: 712px; height: 419px; }
  .card--back  { left: 231px; top: 645px; width: 711px; height: 415px; }

  .brand {
    position: absolute;
    display: flex;
    align-items: center;
    gap: 16px;
  }
  .brand__mark { width: 22px; height: 22px; background: var(--gold); flex: none; }
  .brand__name {
    font-family: "Tinos", "Times New Roman", serif;
    font-weight: 400;
    font-size: 44px;
    line-height: 1.05;
    color: var(--white);
  }
  .card--front .brand { left: 0; right: 0; top: 150px; justify-content: center; }
  .card--back .brand { left: 55px; top: 170px; }
  .card--back .brand__name { font-size: 40px; }

  .specialty__lead {
    position: absolute; left: 0; top: 312px; width: 100%; height: 40px;
    background: var(--white); color: var(--ink);
    font-size: 19px; letter-spacing: 0.3px;
    display: flex; align-items: center; justify-content: center;
  }
  .specialty__list {
    position: absolute; left: 0; top: 352px; width: 100%; height: 38px;
    background: var(--gold); color: var(--ink);
    font-size: 19px; letter-spacing: 0.3px;
    display: flex; align-items: center; justify-content: center;
  }

  .divider {
    position: absolute; left: 356px; top: 45px; width: 1px; height: 275px;
    background: var(--rule);
  }
  .person { position: absolute; left: 397px; top: 82px; }
  .person__name {
    font-family: "Montserrat", Arial, sans-serif; font-weight: 700;
    font-size: 22px; color: var(--gold); letter-spacing: 0.4px;
  }
  .person__role { font-style: italic; font-size: 17px; color: var(--light); margin-top: 6px; letter-spacing: 0.4px; }

  .contacts { position: absolute; left: 396px; top: 208px; list-style: none; }
  .contacts li {
    display: flex; align-items: center; gap: 14px;
    height: 25px; font-size: 18px; color: var(--light); letter-spacing: 0.4px;
  }
  .contacts svg { width: 17px; height: 17px; fill: var(--gold); flex: none; }

  .footer-gold {
    position: absolute; left: 0; bottom: 0; width: 340px; height: 27px;
    background: var(--gold);
  }
  .footer-white {
    position: absolute; right: 0; bottom: 0; width: 380px; height: 53px;
    background: var(--white);
    clip-path: polygon(22px 0, 100% 0, 100% 100%, 0 100%);
  }
  .abn {
    position: absolute; left: 390px; bottom: 14px;
    font-size: 18px; color: var(--ink); letter-spacing: 0.4px;
  }
</style>
</head>
<body>

  <section class="card card--front">
    <div class="brand">
      <span class="brand__mark"></span>
      <span class="brand__name">Tarvale Building Company</span>
    </div>
    <p class="specialty__lead">Specialising in Homes that are:</p>
    <p class="specialty__list">Fire Proof&nbsp;|&nbsp; Climate Proof&nbsp;|&nbsp; Cyclone Rated (Cat. 5)</p>
  </section>

  <section class="card card--back">
    <div class="brand">
      <span class="brand__mark"></span>
      <span class="brand__name">Tarvale<br>Building<br>Company</span>
    </div>

    <div class="divider"></div>

    <div class="person">
      <p class="person__name">Daniel Porter</p>
      <p class="person__role">Managing Director</p>
    </div>

    <ul class="contacts">
      <li>
        <svg viewBox="0 0 16 16" aria-hidden="true"><path d="M4 0h8a1 1 0 0 1 1 1v14a1 1 0 0 1-1 1H4a1 1 0 0 1-1-1V1a1 1 0 0 1 1-1zm1 2v10h6V2zm3 11a1 1 0 1 0 0 2 1 1 0 0 0 0-2z"/></svg>
        <span>0400 555 019</span>
      </li>
      <li>
        <svg viewBox="0 0 16 16" aria-hidden="true"><path d="M1 5c0-2 3-3 7-3s7 1 7 3v1h-4V5H5v1H1zm3 2h8l2 7H2zm4 1.5a2 2 0 1 0 0 4 2 2 0 0 0 0-4z"/></svg>
        <span>(02) 55 501 234</span>
      </li>
      <li>
        <svg viewBox="0 0 16 16" aria-hidden="true"><path d="M1 3h14v1L8 9 1 4zm0 2.5 7 5 7-5V13H1z"/></svg>
        <span>tarvalebuild@mailbox.com</span>
      </li>
    </ul>

    <div class="footer-gold"></div>
    <div class="footer-white"></div>
    <p class="abn">ABN: 12 345 678 901</p>
  </section>

</body>
</html>
```